Flyer-Design für Immobilienmarketing von Raumfreude Home Staging
Zielgruppe
Wir (Raumfreude Home Staging) geben mit Home Staging Immobilien ein Raumfreude (www.raumfreude-beispiel.de). Ziel ist die Immobilienvermarktung zu beschleunigen (Immobilienmarketing) und den besten Preis zu erzielen. Durch ein eigenes Möbel und Dekolager erfolgt die Gestaltung zeitnah.
Zielgruppe sind Immobilienverkäufer (privat) und auch Makler/Vermittler/Projektentwickler
Aufgabenstellung
Wir benötigen einen Flyer/Klappkarte DIN lang quer. Dieser sollte hochwertig, einladend, hell und freundlich erscheinen. Wenn er an der langen Seite gefaltet ist, sollte er als Klappkarte auf dem Tisch stehen können. Dabei sollen alle 4 Seiten genutzt werden. Logo und Design sowie Kurzbeschreibungen/Texte entsprechend bitte der Website (www.raumfreude-beispiel.de) verwenden. Originale können zur Verfügung gestellt werden. Der Flyer sollte auch als PDF nutzbar sein.
Als Slogan stellen wir uns folgendes vor 'Mit Raumfreude in den Immobilienverkauf starten und beim besten Preis landen', sind aber für alles offen. Bei Verwendung von Referenzen wäre ein Spruch mit 'Wohlfühlen' gut. Des Weiteren einfach bei den Texten und Bildern der Website bedienen (Vorteile + warum mit uns) und einen knackigen überzeugenden Flyer bei dem hauptsächlich die Bilder sprechen, erstellen. Wir freuen uns auf die Vorschläge.

```html
<!DOCTYPE html>
<html lang="de">
<head>
<meta charset="utf-8">
<title>Raumfreude Home Staging – Klappkarte</title>
<link href="https://fonts.googleapis.com/css2?family=Questrial&family=Nunito:wght@800&family=Montserrat:wght@300&family=Didact+Gothic&display=swap" rel="stylesheet">
<style>
  :root {
    --stage: #2a2a2a;
    --paper: #ffffff;
    --ink: #3a3a3a;
    --ink-soft: #555555;
    --green: #8dbb2b;
    --box: #dcdcdc;
    --rule: #4a4a4a;
  }
  * { margin: 0; padding: 0; box-sizing: border-box; }
  html, body { width: 1200px; height: 678px; overflow: hidden; background: var(--stage); }
  .canvas { position: relative; width: 1200px; height: 678px; }
  .spread { position: absolute; left: 49px; width: 1102px; height: 262px; background: var(--paper); }
  .spread--outside { top: 59px; }
  .spread--inside { top: 357px; }
  .photo { position: absolute; }
  .contact { position: absolute; left: 28px; top: 82px; font-family: "Didact Gothic", sans-serif; font-size: 5.8px; letter-spacing: 0.6px; color: var(--ink); line-height: 10px; }
  .contact p { margin-bottom: 13.5px; }
  .contact .phone { font-weight: 700; }
  .slogan { position: absolute; left: 934px; top: 50px; width: 160px; }
  .slogan .lead { font-family: "Questrial", sans-serif; font-size: 11.6px; line-height: 13.5px; color: var(--ink); letter-spacing: 0.2px; }
  .slogan .accent { font-family: "Nunito", sans-serif; font-weight: 800; font-size: 13.6px; line-height: 17px; color: var(--green); margin-top: 2px; }
  .slogan .rule { width: 62px; height: 1.5px; background: var(--rule); margin-top: 12px; }
  .brand { position: absolute; left: 932px; top: 182px; display: flex; align-items: center; gap: 6px; font-family: "Questrial", sans-serif; font-size: 24px; color: var(--ink-soft); }
  .brand .dot { width: 9px; height: 9px; border-radius: 50%; background: var(--green); }
  .intro { position: absolute; left: 40px; top: 48px; width: 174px; height: 168px; background: var(--box); padding: 20px 10px 0 18px; font-family: "Questrial", sans-serif; font-size: 5.6px; line-height: 10.8px; color: var(--ink); text-align: center; }
  .service { position: absolute; width: 86px; text-align: center; }
  .service h2 { font-family: "Montserrat", sans-serif; font-weight: 300; font-size: 10.2px; color: var(--ink); letter-spacing: 0.2px; white-space: nowrap; }
  .service hr { border: 0; height: 0.8px; background: var(--ink-soft); margin: 5px 0 6px; }
  .service p { font-family: "Questrial", sans-serif; font-size: 4.9px; line-height: 8.8px; color: var(--ink); }
</style>
</head>
<body>
<div class="canvas">

  <section class="spread spread--outside">
    <div class="contact">
      <p>Lena Marbach-Feld<br>Lindenhofweg 7b<br>22111 Musterstadt</p>
      <p class="phone">PH. 040/123 456 78</p>
      <p>info@raumfreude-beispiel.de</p>
      <p>www.raumfreude-beispiel.de</p>
    </div>
    <div class="photo" style="left:133px;top:15px;width:232px;height:231px;background:linear-gradient(160deg,#ece8e4 0%,#e2dcd6 45%,#8a6a4e 100%)" role="img" aria-label="Hell gestaltetes Arbeitszimmer mit Fenstertür, Regal, Stuhl und Pflanzen"></div>
    <div class="photo" style="left:379px;top:15px;width:530px;height:231px;background:linear-gradient(100deg,#d8d2cc 0%,#e6e1dc 40%,#c9cfd2 65%,#a9b89a 100%)" role="img" aria-label="Wohnzimmer mit Sofa, Couchtisch, blauen Sesseln und großer Fensterfront zum Balkon"></div>
    <div class="slogan">
      <div class="lead">Mit Raumfreude<br>in den Immobilienverkauf</div>
      <div class="accent">starten und beim<br>besten Preis landen'</div>
      <div class="rule"></div>
    </div>
    <div class="brand"><span class="dot"></span>Raumfreude</div>
  </section>

  <section class="spread spread--inside">
    <div class="photo" style="left:195px;top:15px;width:411px;height:231px;background:linear-gradient(120deg,#e4e2df 0%,#dcd8d2 45%,#7b5a40 100%)" role="img" aria-label="Offener Wohnbereich mit Sesseln, Essplatz, Kamin und Leiterregal"></div>
    <div class="intro">
      Unser Ziel ist, die uns anvertraute Immobilie schnell und ganzheitlich so zu gestalten, dass sie alle Sinne eines gemeinsam definierten Zielkunden anspricht. Auf diese Weise ist Home Staging ein wertvolles Instrument der Verkaufs- förderung. Mit einem durchgängigen Konzept, welches sich durch die ganze Immobilie zieht, schaffen wir den optimalen ersten Eindruck und beeinflussen die Kaufentscheidung positiv. Mit unserem Qualitätsanspruch inszenieren wir Wohnräume als Wohnträume.
    </div>
    <div class="photo" style="left:617px;top:15px;width:110px;height:110px;background:linear-gradient(160deg,#eceae7 0%,#d9d6d2 60%,#8a9aa6 100%)" role="img" aria-label="Offene Küche mit Essbereich und Sofa"></div>
    <div class="photo" style="left:739px;top:15px;width:110px;height:110px;background:linear-gradient(160deg,#efefed 0%,#d8d2c8 55%,#2f5a55 100%)" role="img" aria-label="Esstisch mit grünen Samtstühlen vor einer Küchenzeile"></div>
    <div class="photo" style="left:617px;top:137px;width:110px;height:110px;background:linear-gradient(160deg,#b89a4a 0%,#cfc8bf 45%,#6a6a6a 100%)" role="img" aria-label="Wohnzimmer mit Sofa, Wandbild und Teppich"></div>
    <div class="photo" style="left:739px;top:137px;width:110px;height:110px;background:linear-gradient(160deg,#f1f0ee 0%,#d9d9d9 55%,#a58c70 100%)" role="img" aria-label="Helle Küche mit Esstisch und grauen Stühlen"></div>

    <div class="service" style="left:877px;top:43px">
      <h2>HOME STAGING</h2><hr>
      <p>Sie möchten Ihre Immobilie schnell und zum bestmöglichen Preis verkaufen? Wir gestalten Ihre Immobilie zielgerich- tet als das Zuhause, nach dem Käufer suchen.</p>
    </div>
    <div class="service" style="left:990px;top:43px">
      <h2>MIETMÖBEL</h2><hr>
      <p>Mieten oder leasen Sie unsere Möbel, Lampen und Wohnaccessoires und genießen Sie ein ansprechendes Event, Büro oder Zuhause auf Zeit.</p>
    </div>
    <div class="service" style="left:877px;top:157px">
      <h2>PRIVATE SHOPPING</h2><hr>
      <p>Planen und gestalten Sie Ihr Zuhause mit unserem kreativen Interior-Design-Team und bestellen Sie bei uns Ihre ausgewählten Möbel und Wohnaccessoires.</p>
    </div>
    <div class="service" style="left:990px;top:157px">
      <h2>INSTANT HOME</h2><hr>
      <p>Wir richten Ihre Immobilie komplett und in kurzer Zeit mit einem individuellen Raumfreude für Sie ein - zum sofort Wohlfühlen und Einziehen.</p>
    </div>
  </section>

</div>
</body>
</html>
```